Tarrow Building Performance

Id like for my business card to be very bold and professional. Incorporating the business logo, the main services offered, and my contact info. Services are spray foam, insulation, new construction, retrofit, weatherization.

When opening this project sketch harbor was not able to upload my new logo that I picked from another recent sketch harbor project. Does anyone know how i could upload my logo onto the page for design of the business cards?

Target Market(s)

Building owners, contractors

Industry/Entity Type

Building Insulation and performance improvements

Contact Information for Business Card

Owner, Email dean@tarrowbuildingperformance.example Phone number 555-208-6147

Colors
0054AA
0677BA
7BADD7
CADEEF
E8F1F8
F0912C
F2A743
F7CA91
FBE8D2
FDF5EE

Requirements
Must have
• Services- spray foam, cellulose, mineral wool, fiberglass, air sealing, new construction, retrofit, weatherization, energy saving assesments

```html
<!DOCTYPE html>
<html lang="en">
<head>
<meta charset="utf-8">
<title>Tarrow Building Performance – Business Card</title>
<link rel="stylesheet" href="https://fonts.googleapis.com/css2?family=Montserrat:wght@400;500;700;800&display=swap">
<style>
  :root{
    --stage:#2b2b2b;
    --navy:#0b1838;
    --navy-deep:#071029;
    --sky:#3bb0e4;
    --orange:#f07a22;
    --white:#ffffff;
    --ink:#0b1838;
  }
  *{box-sizing:border-box;margin:0;padding:0}
  html,body{width:1200px;height:875px;overflow:hidden}
  body{
    background:var(--stage);
    font-family:"Montserrat",Arial,sans-serif;
    position:relative;
  }
  .card{
    position:absolute;
    top:289px;
    width:520px;height:297px;
    border-radius:18px;
    overflow:hidden;
    box-shadow:0 18px 40px rgba(0,0,0,.45);
  }
  /* back side */
  .card-back{left:50px;background:var(--navy)}
  .card-back .pattern{
    position:absolute;inset:0;
    background:radial-gradient(ellipse at 30% 70%, #16307a 0%, var(--navy) 55%, var(--navy-deep) 100%);
  }
  .card-back .wordmark{
    position:absolute;left:0;right:0;top:50%;
    transform:translateY(-50%);
    display:flex;align-items:center;justify-content:center;gap:14px;
  }
  .wordmark .mark-square{width:22px;height:22px;background:var(--orange)}
  .wordmark .name{
    color:var(--orange);font-weight:800;font-size:27px;line-height:1.05;
    text-transform:uppercase;letter-spacing:.5px;
  }

  /* front side */
  .card-front{left:630px;background:var(--white)}
  .card-front .top{position:absolute;left:0;right:0;top:0;height:178px;background:var(--white)}
  .card-front .band{position:absolute;left:0;right:0;top:178px;height:9px;background:var(--sky)}
  .card-front .bottom{position:absolute;left:0;right:0;top:187px;bottom:0;background:var(--navy)}

  .front-brand{
    position:absolute;left:30px;top:58px;width:200px;
    display:flex;align-items:flex-start;gap:10px;
  }
  .front-brand .mark-square{flex:none;width:18px;height:18px;background:var(--orange);margin-top:4px}
  .front-brand .name{color:var(--orange);font-weight:800;font-size:22px;line-height:1.1;text-transform:uppercase}

  .contact{position:absolute;left:262px;top:30px;width:240px}
  .contact .person{color:var(--sky);font-weight:800;font-size:25px;letter-spacing:.3px;text-transform:uppercase}
  .contact .role{color:var(--orange);font-size:12px;font-weight:500;margin-top:2px}
  .contact .rule{width:40px;height:2px;background:var(--sky);margin:9px 0 10px}
  .contact ul{list-style:none}
  .contact li{display:flex;align-items:center;gap:7px;color:var(--ink);font-size:9.6px;line-height:1.75}
  .contact svg{flex:none;width:10px;height:10px;fill:var(--orange)}

  .services{
    position:absolute;left:22px;right:22px;top:201px;
    color:var(--white);font-size:11px;font-weight:500;text-transform:uppercase;
    text-align:center;line-height:1.75;
  }
  .services .tick{
    display:inline-block;width:10px;height:10px;border-radius:50%;
    background:var(--orange);vertical-align:-1px;margin:0 4px;position:relative;
  }
  .services .tick::after{
    content:"";position:absolute;left:3px;top:1.5px;width:2.5px;height:5px;
    border:solid var(--white);border-width:0 1.4px 1.4px 0;transform:rotate(45deg);
  }
</style>
</head>
<body>

<section class="card card-back" aria-label="Card back">
  <div class="pattern" role="img" aria-label="Tone-on-tone embossed pattern of flame, airflow and snowflake icons"></div>
  <div class="wordmark">
    <span class="mark-square"></span>
    <span class="name">Tarrow<br>Building Performance</span>
  </div>
</section>

<section class="card card-front" aria-label="Card front">
  <div class="top"></div>
  <div class="band"></div>
  <div class="bottom"></div>

  <div class="front-brand">
    <span class="mark-square"></span>
    <span class="name">Tarrow Building Performance</span>
  </div>

  <div class="contact">
    <h1 class="person">Dean Marlow</h1>
    <p class="role">Owner</p>
    <div class="rule"></div>
    <ul>
      <li><svg viewBox="0 0 24 24"><path d="M6.6 10.8a15.1 15.1 0 0 0 6.6 6.6l2.2-2.2a1 1 0 0 1 1-.25 11.4 11.4 0 0 0 3.6.57 1 1 0 0 1 1 1V20a1 1 0 0 1-1 1A17 17 0 0 1 3 4a1 1 0 0 1 1-1h3.5a1 1 0 0 1 1 1c0 1.25.2 2.45.57 3.57a1 1 0 0 1-.25 1z"/></svg>555-208-6147</li>
      <li><svg viewBox="0 0 24 24"><path d="M2 5h20v14H2zm2 2v.5l8 5 8-5V7l-8 5z"/></svg>dean@tarrowbuildingperformance.example</li>
      <li><svg viewBox="0 0 24 24"><path d="M12 2a10 10 0 1 0 0 20 10 10 0 0 0 0-20zm0 3a7 7 0 0 1 6.3 4H14l-2-2-2 3 3 3-1 4-3-3V9L6 8a7 7 0 0 1 6-3z"/></svg>tarrowbuildingperformance.example</li>
    </ul>
  </div>

  <p class="services">
    Spray Foam<span class="tick"></span>Cellulose<span class="tick"></span>Mineral Wool<br>
    Fiberglass<span class="tick"></span>Air Sealing<span class="tick"></span>New Construction<span class="tick"></span>Retrofit<br>
    Weatherization<span class="tick"></span>Energy Saving Assesments
  </p>
</section>

</body>
</html>
```